Industrial Professional Business Card Design (Vantrel Systems)

Would like professional looking business cards. Not too busy leaning towards minimal. Should have a slogan like:
"Industrial Automation and Control".

We are a tech company that programs industrial PLC computers. We also develop custom hardware solutions. Please use the logo for inspiration.

Target Market(s)

Mining, industrial, processing, automation, factory

Industry/Entity Type

Engineering

Contact Information for Business Card

Name, phone, email, website. job title.

Font styles to use
Other font styles liked:
• droid sans

Requirements
Must have
• Use colours that go well with the logo. Not too busy design.

```html
<!DOCTYPE html>
<html lang="en">
<head>
<meta charset="utf-8">
<title>Vantrel Systems — Business Card</title>
<link rel="stylesheet" href="https://fonts.googleapis.com/css2?family=Noto+Sans:wght@400;700&display=swap">
<style>
  :root {
    --backdrop: #2a2a2c;
    --card-white: #ffffff;
    --navy: #1b4a74;
    --navy-deep: #163d61;
    --orange: #f26b21;
    --ink: #1c1c1c;
    --rule: #9a9a9a;
  }
  * { box-sizing: border-box; margin: 0; padding: 0; }
  html, body {
    width: 1200px; height: 1108px; overflow: hidden;
    background: var(--backdrop);
    font-family: "Noto Sans", "Open Sans", sans-serif;
  }
  .stage {
    position: relative; width: 1200px; height: 1108px;
    display: flex; justify-content: center; align-items: center; gap: 70px;
  }
  .card {
    position: relative; width: 400px; height: 686px;
    border-radius: 22px; overflow: hidden;
    box-shadow: 0 14px 30px rgba(0,0,0,.45);
  }
  .card-front { background: var(--card-white); }
  .card-back { background: var(--navy); }

  .brand {
    position: absolute; top: 170px; left: 0; right: 0;
    display: flex; justify-content: center; align-items: center; gap: 12px;
  }
  .brand-dot {
    width: 26px; height: 26px; border-radius: 50%; background: var(--orange);
  }
  .brand-name {
    font-size: 34px; font-weight: 400; color: var(--navy); letter-spacing: .5px;
  }

  .holder { position: absolute; top: 430px; left: 0; right: 0; text-align: center; }
  .holder-name {
    font-size: 27px; font-weight: 700; letter-spacing: .5px; color: var(--navy);
  }
  .holder-name .surname { color: var(--orange); }
  .holder-title { font-size: 19px; color: var(--ink); margin-top: 2px; }

  .icon-row {
    position: absolute; top: 512px; left: 50px; right: 50px;
    display: flex; align-items: center; gap: 10px;
  }
  .icon-row .rule { flex: 1; height: 1px; background: var(--rule); }
  .icon-tile {
    width: 34px; height: 34px; border-radius: 4px; background: var(--navy);
    display: flex; align-items: center; justify-content: center;
  }

  .contact {
    position: absolute; top: 566px; left: 0; right: 0; text-align: center;
    font-size: 19px; line-height: 27px; color: var(--ink);
  }

  .back-brand {
    position: absolute; top: 430px; left: 0; right: 0;
    display: flex; justify-content: center; align-items: center; gap: 10px;
  }
  .back-brand .brand-dot { background: var(--card-white); width: 22px; height: 22px; }
  .back-brand .brand-name { color: var(--card-white); font-size: 28px; }
  .slogan {
    position: absolute; top: 506px; left: 0; right: 0; text-align: center;
    color: var(--card-white); font-size: 22px; line-height: 30px; letter-spacing: .5px;
  }
</style>
</head>
<body>
<main class="stage">
  <section class="card card-front" aria-label="Card front">
    <div class="brand">
      <span class="brand-dot"></span>
      <span class="brand-name">Vantrel Systems</span>
    </div>

    <div class="holder">
      <p class="holder-name">MARCUS <span class="surname">HALE</span></p>
      <p class="holder-title">Managing Director</p>
    </div>

    <div class="icon-row">
      <span class="rule"></span>
      <span class="icon-tile" aria-label="Phone">
        <svg width="20" height="20" viewBox="0 0 24 24"><path fill="#fff" d="M6.6 10.8a15.1 15.1 0 0 0 6.6 6.6l2.2-2.2a1 1 0 0 1 1-.25 11.4 11.4 0 0 0 3.6.57 1 1 0 0 1 1 1V20a1 1 0 0 1-1 1A17 17 0 0 1 3 4a1 1 0 0 1 1-1h3.5a1 1 0 0 1 1 1c0 1.25.2 2.45.57 3.57a1 1 0 0 1-.25 1z"/></svg>
      </span>
      <span class="icon-tile" aria-label="Email">
        <svg width="20" height="20" viewBox="0 0 24 24"><rect x="3" y="6" width="18" height="12" fill="none" stroke="#fff" stroke-width="1.8"/><path d="M3 6l9 7 9-7" fill="none" stroke="#fff" stroke-width="1.8"/></svg>
      </span>
      <span class="icon-tile" aria-label="Website">
        <svg width="20" height="20" viewBox="0 0 24 24"><circle cx="12" cy="12" r="8.5" fill="none" stroke="#fff" stroke-width="1.8"/><ellipse cx="12" cy="12" rx="3.8" ry="8.5" fill="none" stroke="#fff" stroke-width="1.5"/><path d="M3.5 12h17" stroke="#fff" stroke-width="1.5"/></svg>
      </span>
      <span class="rule"></span>
    </div>

    <div class="contact">
      <p>044-987 654 321</p>
      <p>info@vantrelsys.com</p>
      <p>www.vantrelsys.com</p>
    </div>
  </section>

  <section class="card card-back" aria-label="Card back">
    <div class="back-brand">
      <span class="brand-dot"></span>
      <span class="brand-name">Vantrel Systems</span>
    </div>
    <p class="slogan">INDUSTRIAL AUTOMATION<br>AND CONTROL</p>
  </section>
</main>
</body>
</html>
```